Custom Business Card Design

We are looking for a raised spot logo design to use with Tavu.com. We will provide the logo files. Should be a front and back design. We want to implement the house into the back design using the same colors as the logo through out. Something VERY cool!

```html
<!DOCTYPE html>
<html lang="en">
<head>
<meta charset="utf-8">
<title>Tavu Business Card</title>
<link href="https://fonts.googleapis.com/css2?family=Open+Sans:wght@400;600;700&family=Roboto+Condensed:wght@500;700&display=swap" rel="stylesheet">
<style>
  :root {
    --backdrop: #2a2a2c;
    --card: #1f2022;
    --blue: #2f8fd8;
    --red: #e8505b;
    --white: #f2f2f2;
    --divider: #8a8a8a;
  }
  * { margin: 0; padding: 0; box-sizing: border-box; }
  html, body { width: 1200px; height: 900px; overflow: hidden; }
  body {
    background: var(--backdrop);
    font-family: "Open Sans", Arial, sans-serif;
    color: var(--white);
    position: relative;
  }
  .card {
    position: absolute;
    left: 250px;
    width: 700px;
    height: 400px;
    background: var(--card);
  }
  .card-front { top: 35px; }
  .card-back { top: 465px; }

  .brand {
    position: absolute;
    top: 105px;
    left: 0;
    width: 100%;
    text-align: center;
    font-weight: 700;
    font-size: 84px;
    line-height: 1;
    color: var(--blue);
    letter-spacing: 1px;
  }
  .brand-mark {
    display: inline-block;
    width: 22px;
    height: 22px;
    background: var(--red);
    margin-left: 14px;
    vertical-align: middle;
  }
  .front-url {
    position: absolute;
    top: 262px;
    width: 100%;
    text-align: center;
    font-weight: 600;
    font-size: 20px;
  }
  .front-url .accent { color: var(--blue); font-style: italic; }

  .identity {
    position: absolute;
    top: 128px;
    right: 370px;
    text-align: right;
    font-family: "Roboto Condensed", Arial, sans-serif;
  }
  .person-name {
    font-weight: 700;
    font-size: 42px;
    line-height: 1;
    color: var(--blue);
  }
  .person-role {
    margin-top: 8px;
    font-weight: 500;
    font-size: 20px;
    color: var(--red);
    padding-right: 8px;
  }
  .divider {
    position: absolute;
    left: 355px;
    top: 100px;
    width: 2px;
    height: 150px;
    background: var(--divider);
  }
  .contact-list {
    position: absolute;
    left: 380px;
    top: 105px;
    list-style: none;
  }
  .contact-list li {
    display: flex;
    align-items: center;
    height: 27px;
    font-size: 19px;
    font-weight: 600;
  }
  .icon {
    width: 18px;
    height: 18px;
    margin-right: 12px;
    flex: none;
    fill: var(--blue);
  }
  .address {
    position: absolute;
    left: 150px;
    top: 300px;
    display: flex;
    align-items: center;
    font-size: 20px;
    font-weight: 600;
  }
  .address .icon { margin-right: 6px; width: 20px; height: 22px; }
</style>
</head>
<body>
  <section class="card card-front" aria-label="Card front">
    <div class="brand">Tavu<span class="brand-mark"></span></div>
    <div class="front-url">www.<span class="accent">tavu</span>.com</div>
  </section>

  <section class="card card-back" aria-label="Card back">
    <div class="identity">
      <div class="person-name">MARA ELLISON</div>
      <div class="person-role">CEO/FOUNDER</div>
    </div>
    <div class="divider"></div>
    <ul class="contact-list">
      <li>
        <svg class="icon" viewBox="0 0 24 24"><path d="M6.6 10.8a15.1 15.1 0 0 0 6.6 6.6l2.2-2.2c.3-.3.7-.4 1-.2 1.1.4 2.3.6 3.6.6.6 0 1 .4 1 1V20c0 .6-.4 1-1 1C10.6 21 3 13.4 3 4c0-.6.4-1 1-1h3.5c.6 0 1 .4 1 1 0 1.3.2 2.5.6 3.6.1.3 0 .7-.2 1z"/></svg>
        555 210 4471
      </li>
      <li>
        <svg class="icon" viewBox="0 0 24 24"><path d="M7 1h10a2 2 0 0 1 2 2v18a2 2 0 0 1-2 2H7a2 2 0 0 1-2-2V3a2 2 0 0 1 2-2zm0 3v14h10V4zm5 15.5a1.2 1.2 0 1 0 0 2.4 1.2 1.2 0 0 0 0-2.4z"/></svg>
        555 382 9016
      </li>
      <li>
        <svg class="icon" viewBox="0 0 24 24"><path d="M7 2h10v5H7zM4 8h16a2 2 0 0 1 2 2v7h-4v5H6v-5H2v-7a2 2 0 0 1 2-2zm4 8v4h8v-4z"/></svg>
        555 617 2283
      </li>
      <li>
        <svg class="icon" viewBox="0 0 24 24"><path d="M2 5h20v14H2zm2 2v.5l8 5 8-5V7z"/></svg>
        hello@tavu.com
      </li>
      <li>
        <svg class="icon" viewBox="0 0 24 24"><circle cx="12" cy="12" r="10"/><path d="M2 12h20M12 2c3 3 3 17 0 20M12 2c-3 3-3 17 0 20" stroke="#1f2022" stroke-width="1.5" fill="none"/></svg>
        www.tavu.com
      </li>
    </ul>
    <div class="address">
      <svg class="icon" viewBox="0 0 24 24"><path d="M12 1a8 8 0 0 0-8 8c0 6 8 14 8 14s8-8 8-14a8 8 0 0 0-8-8zm0 11a3 3 0 1 1 0-6 3 3 0 0 1 0 6z"/></svg>
      4120 Birchwood Road, Fairbanks, Alaska 99701
    </div>
  </section>
</body>
</html>
```